Website for Torvel Capital - investment banking firm

We have a corporate identity (thanks to Ranjita/41238) and want to extend that into a website design.  See the attached zipped files.
We have software folks in-house to do the coding.
See the attached Project Brief & Notes for more details.  Don't worry about the actual text - lorem ipsum will be fine.
The server will be Apache.
Thank you!
Desmond

```html
<!DOCTYPE html>
<html lang="en">
<head>
<meta charset="utf-8">
<title>Torvel Capital</title>
<link href="https://fonts.googleapis.com/css2?family=Cinzel:wght@400;600;700&family=Open+Sans:wght@400;600;700&display=swap" rel="stylesheet">
<style>
:root{
  --navy:#1f4b8e;
  --navy-dark:#1a4282;
  --link-blue:#1b4c9e;
  --text:#555b61;
  --text-dark:#222;
  --white:#fff;
  --sky-top:#2f6fb4;
  --sky-mid:#a9c6e3;
}
*{box-sizing:border-box;margin:0;padding:0}
html,body{width:879px;height:1200px;overflow:hidden;background:var(--white)}
body{position:relative;font-family:"Open Sans",Arial,sans-serif;color:var(--text)}
.site-header{position:absolute;left:0;top:0;width:879px;height:57px;background:var(--navy)}
.brand{position:absolute;left:114px;top:16px;display:flex;align-items:center;gap:8px;color:var(--white);font-family:"Cinzel",serif;font-weight:600;font-size:15px;letter-spacing:.5px}
.brand-mark{width:20px;height:20px;border:2px solid var(--white);border-radius:50%}
.main-nav{position:absolute;top:23px;left:0;width:879px;font-family:"Cinzel",serif;font-size:10.5px;color:var(--white);letter-spacing:.4px}
.main-nav a{position:absolute;color:inherit;text-decoration:none;white-space:nowrap}
.hero{position:absolute;left:0;top:57px;width:879px;height:276px;
  background:linear-gradient(90deg,#1d3f6e 0%,#2c5f9c 22%,var(--sky-mid) 45%,#d9e6f2 55%,#5b8fc6 75%,#1f4f8c 100%)}
.hero-dots{position:absolute;left:413px;top:255px;display:flex;gap:6px}
.hero-dots span{width:9px;height:9px;border-radius:50%;background:var(--white)}
.hero-dots span.active{background:#2a5aa0}
.intro{position:absolute;left:0;top:352px;width:879px;text-align:center}
.section-title{font-family:"Cinzel",serif;font-weight:600;color:var(--text-dark);font-size:16px;letter-spacing:.5px}
.intro .tagline{margin-top:10px;font-size:10px;font-weight:700;color:var(--link-blue)}
.intro p.lead{width:640px;margin:6px auto 0;font-size:10.3px;line-height:18.5px;color:var(--text-dark)}
.about{position:absolute;left:122px;top:477px;width:310px}
.about p{margin-top:16px;font-size:9.6px;line-height:16.2px}
.global{position:absolute;left:446px;top:477px;width:320px}
.map{position:absolute;left:18px;top:41px;width:262px;height:130px;border-radius:40px;
  background:radial-gradient(ellipse at 50% 50%,#2e6fe0 0%,#3d7ff0 55%,rgba(255,255,255,0) 75%)}
.services-title{position:absolute;left:0;top:686px;width:879px;text-align:center}
.service{position:absolute;top:729px;width:150px}
.service .photo{width:150px;height:93px}
.service h3{margin-top:18px;font-family:"Cinzel",serif;font-weight:700;font-size:9.6px;color:var(--text-dark);letter-spacing:.3px;padding-left:2px}
.service p{margin-top:10px;font-size:9.6px;line-height:16.2px}
.btn{display:inline-block;margin-top:12px;width:73px;height:25px;line-height:25px;text-align:center;background:var(--navy-dark);color:var(--white);font-size:10px;font-weight:700;text-decoration:none}
.site-footer{position:absolute;left:0;top:1038px;width:879px;height:162px;background:var(--navy);color:var(--white);font-size:9.6px}
.footer-note{position:absolute;top:12px;left:0;width:879px;text-align:center;font-weight:700;line-height:16.5px}
.office{position:absolute;top:58px;text-align:center;line-height:16.5px}
.office b{font-weight:700}
.copyright{position:absolute;top:132px;left:0;width:879px;text-align:center}
</style>
</head>
<body>
<header class="site-header">
  <div class="brand"><span class="brand-mark"></span>Torvel Capital</div>
  <nav class="main-nav">
    <a style="left:302px" href="#">Home</a>
    <a style="left:357px" href="#">About</a>
    <a style="left:414px" href="#">Services</a>
    <a style="left:482px" href="#">Current Engagements</a>
    <a style="left:628px" href="#">Completed Transactions</a>
  </nav>
</header>

<section class="hero" role="img" aria-label="Upward view of glass office towers against a blue cloudy sky">
  <div class="hero-dots"><span class="active"></span><span></span><span></span><span></span></div>
</section>

<section class="intro">
  <h1 class="section-title">Welcome to Torvel Capital</h1>
  <p class="tagline">Global, Professional, Trusted ... or Disciplined / Effective?</p>
  <p class="lead">Torvel Capital is an independent investment bank working for buyers in a number of industries. We utilize exceptional technology in finding companies to meet our client's search criteria. We will not waste a buyer's time, a seller's time, or our own time.</p>
</section>

<section class="about">
  <h2 class="section-title">Whom We Are</h2>
  <p>Lorem ipsum dolor sit amet, consectetur adipisicing elit, sed do eiusmod tempor incididunt ut labore et dolore magna aliqua. Ut enim ad minim veniam, quis nostrud exercitation ullamco laboris nisi ut aliquip ex ea commodo consequat. Duis aute irure dolor in reprehenderit in voluptate velit esse cillum dolore eu fugiat nulla pariatur. Excepteur sint occaecat cupidatat non proident, sunt in culpa qui officia deserunt mollit anim id est laborum.<br>Lorem ipsum dolor sit amet, consectetur adipisicing elit, sed do eiusmod tempor incididunt ut labore et dolore magna aliqua.</p>
</section>

<section class="global">
  <h2 class="section-title">Global Investment Banking Services</h2>
  <div class="map" role="img" aria-label="Blue world map showing global coverage"></div>
</section>

<h2 class="section-title services-title">Our Services</h2>

<article class="service" style="left:122px">
  <div class="photo" role="img" aria-label="Oil pump jacks at sunset" style="background:linear-gradient(180deg,#5b88c4 0%,#c9b892 65%,#4a3a24 100%)"></div>
  <h3>Oilfield Services</h3>
  <p>Lorem ipsum dolor sit amet, con-sectetur adipisicing elit, sed do eiusmod tempor incididunt ut labore et dolore magna aliqua. Ut enim ad minim veniam, quis nos-trud exercitation ullamco</p>
  <a class="btn" href="#">Read More</a>
</article>

<article class="service" style="left:282px">
  <div class="photo" role="img" aria-label="Workers operating machinery in a manufacturing plant" style="background:linear-gradient(135deg,#8f969b 0%,#c2c6c8 50%,#5e6569 100%)"></div>
  <h3>Oilfield Manufacturing</h3>
  <p>Lorem ipsum dolor sit amet, con-sectetur adipisicing elit, sed do eiusmod tempor incididunt ut labore et dolore magna aliqua. Ut enim ad minim veniam, quis nos-trud exercitation ullamco</p>
  <a class="btn" href="#">Read More</a>
</article>

<article class="service" style="left:445px">
  <div class="photo" role="img" aria-label="Business meeting around a boardroom table" style="background:linear-gradient(180deg,#d8d2c8 0%,#b9a890 60%,#7a6450 100%)"></div>
  <h3>Asset Managment</h3>
  <p>Lorem ipsum dolor sit amet, con-sectetur adipisicing elit, sed do eiusmod tempor incididunt ut labore et dolore magna aliqua. Ut enim ad minim veniam, quis nos-trud exercitation ullamco</p>
  <a class="btn" href="#">Read More</a>
</article>

<article class="service" style="left:609px">
  <div class="photo" role="img" aria-label="Professionals seated at a business seminar" style="background:linear-gradient(180deg,#cfc8c0 0%,#8c7a6c 55%,#3a3432 100%)"></div>
  <h3>Insurance Brokerage</h3>
  <p>Lorem ipsum dolor sit amet, con-sectetur adipisicing elit, sed do eiusmod tempor incididunt ut labore et dolore magna aliqua. Ut enim ad minim veniam, quis nos-trud exercitation ullamco</p>
  <a class="btn" href="#">Read More</a>
</article>

<footer class="site-footer">
  <p class="footer-note">Torvel Capital maintains offices in China, Japan, the USA and Canada. We will respond<br>to your enquiries rapidly. Please contact us at the email address below.</p>
  <div class="office" style="left:162px;width:186px;top:57px"><b>Hong Kong:</b> Room 1804 Harbourline Tower<br>28 - 36 Kellet Road East<br>Wanchai, Hong Kong</div>
  <div class="office" style="left:368px;width:172px"><b>Dallas:</b> 4100 Meridian Parkway, Suite 210<br>Plano, Texas 75024<br>Telephone: 469-555-0172</div>
  <div class="office" style="left:570px;width:152px;top:74px">E-mail: info@torvelcapital.com</div>
  <p class="copyright">© 2014 Company Name ,All Rights reserved</p>
</footer>
</body>
</html>
```